The Plate Compass

Cutting Through the Noise to What Actually Works.

Nutrition book

Target Market(s)

People looking to be or get healthy and eat right.

```html
<!DOCTYPE html>
<html lang="en">
<head>
<meta charset="utf-8">
<title>The Plate Compass — Book Cover</title>
<link href="https://fonts.googleapis.com/css2?family=Poppins:wght@700;800&family=Montserrat:wght@400;500;700;800&family=Caveat:wght@400&display=swap" rel="stylesheet">
<style>
  :root {
    --paper: #f4f4f3;
    --paper-shade: #e9e9e8;
    --ink-green: #066838;
    --scribble-grey: #8d8d8d;
    --ring-1: #fffaeb;
    --ring-2: #fff4d2;
    --ring-3: #ffedb4;
    --ring-4: #ffe58f;
    --core: #fde01f;
    --core-edge: #fbe46a;
    --rim-shadow: #6b5e4c;
    --ring-label: #e8a33a;
    --ring-label-soft: #efbd66;
    --author-ink: #3a3a3a;
    --white: #ffffff;
  }
  * { margin: 0; padding: 0; box-sizing: border-box; }
  html, body { width: 800px; height: 1200px; overflow: hidden; background: var(--paper); }
  .cover {
    position: relative;
    width: 800px;
    height: 1200px;
    overflow: hidden;
    background: var(--paper);
  }
  .noise-field {
    position: absolute;
    inset: 0 0 auto 0;
    height: 720px;
    background: radial-gradient(ellipse at 50% 40%, var(--paper) 0%, var(--paper-shade) 100%);
  }
  .buzzword {
    position: absolute;
    font-family: "Caveat", cursive;
    color: var(--scribble-grey);
    font-size: 30px;
    line-height: 1;
  }
  .buzzword--vitamins { left: 458px; top: 38px; transform: rotate(-4deg); }
  .buzzword--keto { left: 12px; top: 228px; transform: rotate(-6deg); }
  .buzzword--detox { left: 702px; top: 196px; transform: rotate(-10deg); }
  .buzzword--lowcarb { left: 130px; top: 420px; transform: rotate(-8deg); }
  .buzzword--sugar { left: 644px; top: 448px; transform: rotate(-14deg); }

  .title-block {
    position: absolute;
    left: 0; right: 0; top: 170px;
    text-align: center;
    color: var(--ink-green);
  }
  .title-lockup {
    display: inline-block;
    text-align: left;
  }
  .title-the {
    display: block;
    font-family: "Montserrat", sans-serif;
    font-weight: 500;
    font-size: 28px;
    line-height: 28px;
    letter-spacing: 5px;
    padding-left: 6px;
  }
  .title-main {
    font-family: "Poppins", sans-serif;
    font-weight: 800;
    font-size: 138px;
    line-height: 110px;
    letter-spacing: -3px;
  }
  .title-sub {
    display: flex;
    justify-content: space-between;
    width: 642px;
    margin: 14px auto 0;
    font-family: "Montserrat", sans-serif;
    font-weight: 400;
    font-size: 44px;
    line-height: 1;
  }
  .tagline {
    margin-top: 14px;
    font-family: "Montserrat", sans-serif;
    font-weight: 500;
    font-size: 24.5px;
    line-height: 1.1;
  }

  .target {
    position: absolute;
    inset: 0;
    width: 800px;
    height: 1200px;
  }
  .ring-label {
    font-family: "Montserrat", sans-serif;
    font-weight: 700;
    font-size: 31px;
    letter-spacing: 3px;
  }
  .ring-label--strong { fill: var(--ring-label); }
  .ring-label--soft { fill: var(--ring-label-soft); }
  .core-label {
    font-family: "Montserrat", sans-serif;
    font-weight: 700;
    font-size: 35px;
    letter-spacing: 3px;
    fill: var(--white);
  }
  .author {
    position: absolute;
    left: 0; right: 0; top: 1080px;
    text-align: center;
    font-family: "Montserrat", sans-serif;
    font-weight: 700;
    font-size: 41px;
    line-height: 50px;
    color: var(--author-ink);
  }
</style>
</head>
<body>
<main class="cover">
  <div class="noise-field" role="img" aria-label="Tangled hand-drawn grey scribble lines representing confusing diet noise"></div>
  <span class="buzzword buzzword--vitamins">vitamins</span>
  <span class="buzzword buzzword--keto">keto</span>
  <span class="buzzword buzzword--detox">detox</span>
  <span class="buzzword buzzword--lowcarb">low carb</span>
  <span class="buzzword buzzword--sugar">sugar</span>

  <header class="title-block">
    <div class="title-lockup">
      <span class="title-the">THE</span>
      <h1 class="title-main">Plate</h1>
    </div>
    <div class="title-sub"><span>C</span><span>O</span><span>M</span><span>P</span><span>A</span><span>S</span><span>S</span></div>
    <p class="tagline">Cutting Through the Noise to What Actually Works</p>
  </header>

  <svg class="target" viewBox="0 0 800 1200" aria-hidden="true">
    <defs>
      <filter id="rim-blur" x="-20%" y="-20%" width="140%" height="140%">
        <feGaussianBlur stdDeviation="7"/>
      </filter>
      <radialGradient id="core-fill" cx="50%" cy="45%" r="50%">
        <stop offset="0%" stop-color="var(--core)"/>
        <stop offset="70%" stop-color="var(--core)"/>
        <stop offset="100%" stop-color="var(--core-edge)"/>
      </radialGradient>
      <linearGradient id="base-fade" x1="0" y1="0" x2="0" y2="1">
        <stop offset="0%" stop-color="var(--ring-1)" stop-opacity="0"/>
        <stop offset="100%" stop-color="var(--ring-1)" stop-opacity="0.8"/>
      </linearGradient>
      <path id="arc-supplements" d="M -10 980 A 410 410 0 0 1 810 980"/>
      <path id="arc-meal" d="M 50 980 A 350 350 0 0 1 750 980"/>
      <path id="arc-food" d="M 117 980 A 283 283 0 0 1 683 980"/>
      <path id="arc-protein" d="M 178 980 A 222 222 0 0 1 622 980"/>
    </defs>
    <circle class="rim-shadow" cx="400" cy="974" r="472" fill="var(--rim-shadow)" filter="url(#rim-blur)"/>
    <circle cx="400" cy="980" r="469" fill="var(--ring-1)"/>
    <circle cx="400" cy="980" r="400" fill="var(--ring-2)"/>
    <circle cx="400" cy="980" r="329" fill="var(--ring-3)"/>
    <circle cx="400" cy="980" r="262" fill="var(--ring-4)"/>
    <circle cx="400" cy="980" r="209" fill="url(#core-fill)"/>
    <rect x="0" y="1060" width="800" height="140" fill="url(#base-fade)"/>

    <text class="ring-label ring-label--strong" text-anchor="middle"><textPath href="#arc-supplements" startOffset="50%">SUPPLEMENTS</textPath></text>
    <text class="ring-label ring-label--soft" text-anchor="middle"><textPath href="#arc-meal" startOffset="50%">MEAL TIMING</textPath></text>
    <text class="ring-label ring-label--strong" text-anchor="middle"><textPath href="#arc-food" startOffset="50%">FOOD QUALITY</textPath></text>
    <text class="ring-label ring-label--strong" text-anchor="middle"><textPath href="#arc-protein" startOffset="50%">PROTEIN</textPath></text>
    <text class="core-label" x="400" y="927" text-anchor="middle">CALORIES</text>
  </svg>

  <p class="author">AUTHOR NAME</p>
</main>
</body>
</html>
```